Energy and Environment Venture Capital Blog

Look for an out of the box creative design!

I am working on putting together a new blog / website with a few colleagues in the cleantech / energy venture capital space. I would like to push the box on design and get really creative for how to display the following (very simple):

1) Updated News on venture capital and cleantech (rss feed)
2) Would also like to have a profile page to feature "company of the month"
2.1) Included in this page I would like to be able to have a gallery of photos and have it be an interactive profile of company that includes:
2.1.1) Funding received to date, funders, location, founders (really good example of this is would be on greenledgerhub.com. (there may even be a way to take the date right from their website)
EXTRA: would be amazing to be able to place all the selected company on a map
3) Blog entries that can include photos and movies and active commenting
4) Resources section for interesting websites, books, surveys etc. (pageharbor)
5) Would like to be able to link my social media (chirpline, friendwall)

A couple good examples include:

http://www.moslantic.co.uk/
http://www.copperwindmade.co.uk/
http://www.tarvel-nook.com/

Note: I have a logo designed for the website that I can send across. I also have a domain name registered at http://q7fundloft.com/

I have also attached the draft logo to show the colors I am hoping to use across the site.
Updates

Project Deadline Extended
Reason: Really want to make sure that we get the design right and dont want to have to rush things. If however I find a design concept I like I am happy to pull the trigger right away and work outside the contest.

Target Market(s)

venture capitalists, technologists, SMEs

Industry/Entity Type

Venture Capital

Requirements
Must have
• A funky and creative landing page
The profile page (I would like it to be called Q7 Profiles) should be the feature section of the website
Nice to have
• What I was hoping to do (if possible) was to create a stock index that tracks some of the leading cleantech stocks on the market. Done know if there is anything out there that is open source but if there is I would love a section on the blog called "Q7 Index"
Should not have
• The design should not use old-style, serif fonts like Times New Roman.

```html
<!DOCTYPE html>
<html lang="en">
<head>
<meta charset="utf-8">
<title>q7fundloft</title>
<link href="https://fonts.googleapis.com/css2?family=Open+Sans:wght@400;600&family=Questrial&display=swap" rel="stylesheet">
<style>
:root{
  --page:#d8d8d6;
  --panel:#efefef;
  --panel-line:#c9c9c9;
  --green:#6aa521;
  --green-dark:#4f8514;
  --green-light:#86bd35;
  --ink:#333;
  --ink-soft:#555;
  --grey-badge:#9a9a9a;
  --btn-dark:#4a4f55;
  --white:#fff;
}
*{box-sizing:border-box;margin:0;padding:0}
html,body{width:1200px;height:2679px;overflow:hidden}
body{position:relative;background:var(--page);font-family:"Open Sans",Arial,sans-serif;color:var(--ink)}
.abs{position:absolute}
.site-header{left:0;top:0;width:1200px;height:176px;background:linear-gradient(#fafafa,#dedede);border-bottom:1px solid #bdbdbd}
.brand{left:68px;top:64px;font-family:"Questrial",sans-serif;font-size:54px;color:#666;display:flex;align-items:center;gap:14px}
.brand-dot{width:16px;height:16px;border-radius:50%;background:var(--green)}
.social{display:flex;gap:8px}
.social span{width:32px;height:32px;border-radius:4px;background:#6d6d6d}
.header-social{left:1006px;top:16px}
.search{left:905px;top:72px;width:256px;height:34px;background:var(--white);border:1px solid #ccc}
.search svg{position:absolute;right:6px;top:5px}
.main-nav{left:32px;top:206px;width:1134px;height:52px;background:linear-gradient(var(--green-light),var(--green));border-top:3px solid var(--green-dark);border-bottom:3px solid var(--green-dark);display:flex;align-items:center;padding-left:74px;gap:46px}
.main-nav a,.footer-nav a{font-family:"Questrial",sans-serif;font-size:21px;color:var(--white);text-decoration:none}
.hero{left:32px;top:277px;width:1134px;height:571px;background:var(--white);padding:13px}
.hero-img{width:100%;height:100%;background:linear-gradient(#3f7fd1 0%,#8cb9ee 55%,#b9c77e 85%,#6e8a32 100%);position:relative}
.hero-caption{position:absolute;left:0;right:0;bottom:0;height:108px;background:rgba(90,90,90,.55);color:var(--white);font-size:29px;line-height:43px;padding:12px 38px;font-weight:400}
.panel{background:var(--panel);border:1px solid var(--panel-line);padding:12px}
.panel-inner{position:relative;width:100%;height:100%;border:1px dashed #c4c4c4}
.panel h2{position:absolute;left:18px;top:16px;font-weight:400;font-size:26px;color:#222}
.small{font-size:13.5px;line-height:26px;color:var(--ink-soft)}
.avatar{left:20px;top:62px;width:125px;height:133px;background:linear-gradient(#6fa3d6,#2c4f7a);border:2px solid var(--white);box-shadow:0 0 2px #999}
.about-lead{left:150px;top:86px;font-size:23px;line-height:29px;color:#333;width:220px}
.about-text{left:20px;top:222px;width:345px}
.link{color:#444;text-decoration:underline}
.field{left:20px;top:116px;width:334px;height:36px;background:var(--white);border:1px solid #bbb}
.btn-subscribe{left:126px;top:180px;width:122px;height:32px;background:#7a7a7a;color:var(--white);font-size:18px;text-align:center;line-height:32px}
.company{top:76px;width:155px;height:108px;background:var(--white);border:1px solid #ccc;display:flex;align-items:center;justify-content:center;gap:8px;font-size:22px;font-weight:600;color:#555}
.company i{width:12px;height:12px;background:#999;display:block}
.members{left:20px;top:92px;width:334px;height:178px;background:linear-gradient(135deg,#c9a68e,#8aa0b4 50%,#d7c25a);border:6px solid var(--white);box-shadow:0 0 2px #aaa}
.date-badge{right:18px;top:18px;padding:0 12px;height:30px;line-height:30px;background:var(--grey-badge);color:var(--white);font-size:13px}
.post-img{left:22px;top:84px;width:602px;height:401px}
.post-text{left:22px;top:500px;width:602px}
.post-meta{left:22px;top:676px;width:613px;height:28px;background:var(--green);color:var(--white);font-size:14px;line-height:28px;padding:0 12px;display:flex;justify-content:space-between}
.pager{left:588px;top:2427px;display:flex;gap:14px}
.pager span{height:36px;min-width:34px;padding:0 10px;background:var(--btn-dark);color:var(--white);font-size:16px;font-weight:600;line-height:36px;text-align:center;border-radius:3px}
.site-footer{left:0;top:2487px;width:1200px;height:192px;background:linear-gradient(var(--green-light),var(--green))}
.footer-nav{position:absolute;left:0;width:1200px;top:20px;display:flex;justify-content:center;gap:46px}
.footer-social{left:492px;top:73px}
.copyright{position:absolute;left:0;width:1200px;top:134px;text-align:center;color:var(--white);font-size:13.5px}
</style>
</head>
<body>
<header class="abs site-header">
  <div class="abs brand"><span>q7fundloft</span><i class="brand-dot"></i></div>
  <div class="abs social header-social"><span></span><span></span><span></span><span></span></div>
  <div class="abs search"><svg width="26" height="26" viewBox="0 0 26 26"><circle cx="10" cy="10" r="7" fill="none" stroke="#222" stroke-width="3"/><line x1="15" y1="15" x2="23" y2="23" stroke="#222" stroke-width="3"/></svg></div>
</header>

<nav class="abs main-nav">
  <a href="#">Home</a><a href="#">About Us</a><a href="#">Forum</a><a href="#">Recent Blog Post</a><a href="#">Companies of the month</a><a href="#">Contact Us</a>
</nav>

<section class="abs hero">
  <div class="hero-img" role="img" aria-label="Person sitting on a wooden bench under a blue sky">
    <p class="hero-caption">But I must explain to you how all this mistaken idea of denouncing pleasure and praising pain account of the system,</p>
  </div>
</section>

<aside>
  <div class="abs panel" style="left:37px;top:868px;width:403px;height:482px"><div class="panel-inner">
    <h2>About Me</h2>
    <div class="abs avatar" role="img" aria-label="Profile photo"></div>
    <p class="abs about-lead">Sed ut perspiciatis unde omnis iste natus</p>
    <p class="abs about-text small">Sed ut perspiciatis unde omnis iste natus error sit voluptatem accusantium doloremque laudantium, totam rem aperiam, eaque ipsa quae ab illo inventore veritatis et quasi architecto beatae vitae dicta sunt explicabo.<br><span class="link">info@q7fundloft.com</span></p>
    <p class="abs small link" style="right:18px;top:406px">View my complete profile</p>
  </div></div>

  <div class="abs panel" style="left:37px;top:1378px;width:403px;height:252px"><div class="panel-inner">
    <h2>Subscribe Newsletter</h2>
    <p class="abs small" style="left:20px;top:78px">Enter your email address:</p>
    <div class="abs field"></div>
    <div class="abs btn-subscribe">Subscribe</div>
  </div></div>

  <div class="abs panel" style="left:37px;top:1652px;width:403px;height:253px"><div class="panel-inner">
    <h2>Companies of the month</h2>
    <div class="abs company" style="left:26px"><i></i>Voltaris</div>
    <div class="abs company" style="left:193px"><i></i>Helionix</div>
  </div></div>

  <div class="abs panel" style="left:37px;top:1940px;width:403px;height:336px"><div class="panel-inner">
    <h2>Join this site</h2>
    <p class="abs small" style="left:20px;top:58px">Members (28)</p>
    <p class="abs small" style="right:20px;top:58px">More »</p>
    <div class="abs members" role="img" aria-label="Grid of member profile pictures"></div>
    <p class="abs" style="left:20px;top:286px;font-size:14px;color:#444">Already a member? Sign in</p>
  </div></div>
</aside>

<main>
  <article class="abs panel" style="left:473px;top:865px;width:695px;height:770px"><div class="panel-inner">
    <h2 style="top:34px">Recent Posts</h2>
    <div class="abs date-badge">Monday, 14 November 2011</div>
    <div class="abs post-img" role="img" aria-label="Two clasped hands over green grass" style="background:linear-gradient(135deg,#4f7d2a,#e8b89c 40%,#f1c7ad 60%,#5a8a2e)"></div>
    <p class="abs post-text small">At vero eos et accusamus et iusto odio dignissimos ducimus qui blanditiis praesentium voluptatum deleniti atque corrupti quos dolores et quas molestias excepturi sint occaecati cupiditate non provident, similique sunt in culpa qui officia deserunt mollitia animi, id est laborum et dolorum fuga. Et harum At vero eos et accusamus et iusto odio dignissimos ducimus qui blanditiis praesentium voluptatum deleniti atque corrupti quos dolores et quas molestias excepturi sint occaecati cupiditate non</p>
    <div class="abs post-meta"><span>Posted by at 6:13 PM</span><span>2 comments</span></div>
  </div></article>

  <article class="abs panel" style="left:473px;top:1650px;width:695px;height:770px"><div class="panel-inner">
    <h2 style="top:34px">Latest Post</h2>
    <div class="abs date-badge">Monday, 14 November 2011</div>
    <div class="abs post-img" role="img" aria-label="Woman in white dress sitting by a stream" style="background:linear-gradient(#6f9a3a,#a9c56a 45%,#d9d5c8 60%,#6b8f3d)"></div>
    <p class="abs post-text small">At vero eos et accusamus et iusto odio dignissimos ducimus qui blanditiis praesentium voluptatum deleniti atque corrupti quos dolores et quas molestias excepturi sint occaecati cupiditate non provident, similique sunt in culpa qui officia deserunt mollitia animi, id est laborum et dolorum fuga. Et harum At vero eos et accusamus et iusto odio dignissimos ducimus qui blanditiis praesentium voluptatum deleniti atque corrupti quos dolores et quas molestias excepturi sint occaecati cupiditate non</p>
    <div class="abs post-meta"><span>Posted by at 6:13 PM</span><span>2 comments</span></div>
  </div></article>

  <nav class="abs pager"><span>Prev</span><span>1</span><span>2</span><span>3</span><span>4</span><span>5</span><span>6</span><span>…</span><span>22</span><span>Next</span></nav>
</main>

<footer class="abs site-footer">
  <nav class="footer-nav"><a href="#">Home</a><a href="#">About Us</a><a href="#">Forum</a><a href="#">Recent Blog Post</a><a href="#">Companies of the month</a><a href="#">Contact Us</a></nav>
  <div class="abs social footer-social"><span></span><span></span><span></span><span></span></div>
  <p class="copyright">Copyright @ 2013.www.q7fundloft.com . All Rights Reserved.</p>
</footer>
</body>
</html>
```